Harvest of Kingdoms
preparing the way of the Lord...
Modern
Tom Farrel
412 Co.Rd. 118 Marlow, Pa.17602
tomjane4Faith@postvale.com
www.tf-harvestofkingdoms.com
preaching the gospel of Jesus, and teaching others to do the same.
mission trips
rallies and revivals
camps
this is for business cards and letterhead...

```html
<!DOCTYPE html>
<html lang="en">
<head>
<meta charset="utf-8">
<title>Harvest of Kingdoms – Business Cards</title>
<link href="https://fonts.googleapis.com/css2?family=Marcellus&family=Open+Sans:wght@400;600&display=swap" rel="stylesheet">
<style>
  :root {
    --backdrop: #ece8e2;
    --card: #ffffff;
    --ink: #1f2a33;
    --ink-soft: #4a545c;
    --sage: #dfe9d6;
    --sage-deep: #c9d9bd;
    --bar: #eef3ea;
    --halo: #dfe8ee;
  }
  * { box-sizing: border-box; margin: 0; padding: 0; }
  html, body { width: 1200px; height: 427px; overflow: hidden; }
  body {
    background: var(--backdrop);
    font-family: "Open Sans", Arial, sans-serif;
    color: var(--ink);
    position: relative;
  }
  .card {
    position: absolute;
    top: 84px;
    width: 505px;
    height: 300px;
    background: var(--card);
    border-radius: 14px;
    overflow: hidden;
    box-shadow: 0 2px 8px rgba(0,0,0,.12);
  }
  .card--front { left: 70px; }
  .card--back { left: 622px; }

  .brand {
    position: absolute;
    left: 0; right: 0;
    text-align: center;
    font-family: "Marcellus", Georgia, serif;
    font-weight: 400;
    color: var(--ink);
    line-height: 1;
  }
  .brand__small { display: block; font-size: 24px; padding-left: 150px; }
  .brand__large { display: block; font-size: 48px; letter-spacing: 1px; margin-top: 2px; }
  .card--front .brand { top: 40px; }
  .card--back .brand { top: 40px; }

  .band-vertical {
    position: absolute;
    left: 62px; top: 0; bottom: 0;
    width: 34px;
    background: linear-gradient(to right, var(--sage), var(--sage-deep));
    opacity: .8;
  }
  .name-bar {
    position: absolute;
    left: 0; right: 0;
    top: 148px;
    height: 34px;
    background: linear-gradient(to right, var(--sage-deep), var(--bar) 30%, var(--card));
    display: flex;
    align-items: center;
    justify-content: center;
    font-size: 13px;
    gap: 8px;
  }
  .name-bar__person { font-weight: 600; letter-spacing: .5px; text-transform: uppercase; }
  .name-bar__divider { color: var(--ink-soft); }
  .name-bar__org { color: var(--ink-soft); }

  .contact {
    position: absolute;
    left: 0; right: 0;
    top: 194px;
    text-align: center;
    font-size: 11.5px;
    color: var(--ink-soft);
    line-height: 24px;
  }
  .contact__row { display: flex; justify-content: center; align-items: center; gap: 6px; }
  .contact__row + .contact__row { }
  .contact__icon { width: 11px; height: 11px; fill: var(--ink); }
  .contact__gap { width: 16px; }

  .halo {
    position: absolute;
    left: 128px; top: 70px;
    width: 220px; height: 220px;
    border-radius: 50%;
    background: radial-gradient(circle, var(--halo), rgba(223,232,238,.25));
  }
  .mission {
    position: absolute;
    right: 28px;
    top: 186px;
    width: 310px;
    text-align: center;
    font-size: 12px;
    color: var(--ink-soft);
    line-height: 17px;
  }
  .ministries {
    position: absolute;
    left: 120px; right: 20px;
    top: 232px;
    display: flex;
    justify-content: center;
    gap: 22px;
    font-size: 12px;
    color: var(--ink-soft);
    list-style: none;
  }
  .ministries li::before { content: "•"; margin-right: 5px; color: var(--ink); }
  .web {
    position: absolute;
    left: 0; right: 0;
    bottom: 22px;
    display: flex; justify-content: center; align-items: center; gap: 6px;
    font-size: 11px;
    color: var(--ink-soft);
  }
</style>
</head>
<body>
  <section class="card card--front">
    <div class="band-vertical"></div>
    <h1 class="brand"><span class="brand__small">Harvest of</span><span class="brand__large">KINGDOMS</span></h1>
    <div class="name-bar">
      <span class="name-bar__person">Tom Farrel</span>
      <span class="name-bar__divider">|</span>
      <span class="name-bar__org">Harvest of Kingdoms</span>
    </div>
    <div class="contact">
      <p class="contact__row">412 Co.Rd. 118 Marlow, Pa.17602</p>
      <p class="contact__row">
        <svg class="contact__icon" viewBox="0 0 12 12"><path d="M2.5 1h2l1 2.5-1.3 1a6 6 0 0 0 3.3 3.3l1-1.3L11 7.5v2A1.5 1.5 0 0 1 9.5 11 8.5 8.5 0 0 1 1 2.5 1.5 1.5 0 0 1 2.5 1z"/></svg>
        <span>570.316.2904</span>
        <span class="contact__gap"></span>
        <svg class="contact__icon" viewBox="0 0 12 12"><circle cx="6" cy="6" r="5" fill="none" stroke="currentColor" stroke-width="1.4"/><circle cx="6" cy="6" r="2"/></svg>
        <span>tomjane4Faith@postvale.com</span>
      </p>
      <p class="contact__row">
        <svg class="contact__icon" viewBox="0 0 12 12"><path d="M6 1 1 5h1.5v5h7V5H11z"/></svg>
        <span>www.tf-harvestofkingdoms.com</span>
      </p>
    </div>
  </section>

  <section class="card card--back">
    <div class="halo"></div>
    <h2 class="brand"><span class="brand__small">Harvest of</span><span class="brand__large">KINGDOMS</span></h2>
    <p class="mission">preaching the gospel of Jesus,<br>and teaching others to do the same.</p>
    <ul class="ministries">
      <li>mission trips</li>
      <li>rallies and revivals</li>
      <li>camps</li>
    </ul>
    <p class="web">
      <svg class="contact__icon" viewBox="0 0 12 12"><path d="M6 1 1 5h1.5v5h7V5H11z"/></svg>
      <span>www.tf-harvestofkingdoms.com</span>
    </p>
  </section>
</body>
</html>
```